Professional Services - letterhead / business cards

The company (veltaro holdings) will provide services to Investment Funds and large investors in Spain. I have recently chosen a logo that I am attaching.

I would like a simple stationary design that i could use as letter head, business cards and "with compliments" cards.

I am not quite sure which color I will mostly use for the logo, in the email signature I will probably lean towards the white background and grey letters. I am attaching my favourite options.

Target Market(s)

Large Multinationals, Investment funds and Law firms

Industry/Entity Type

Business

Requirements
Must have
• my details are:
Luis R. Andrade
Veltaro Holdings S.L.
Casa de Valdehondo
Calle del Olmo Tardío 42
28017 Madrid
T: +34 (91) 807-3356
M: +34 (655) 718-904
e-mail: landrade@veltaroholdings.example

```html
<!DOCTYPE html>
<html lang="en">
<head>
<meta charset="utf-8">
<title>Veltaro Holdings – Business Card</title>
<link rel="stylesheet" href="https://fonts.googleapis.com/css2?family=Jost:wght@400;500;600&display=swap">
<style>
  :root {
    --backdrop: #2b2b2d;
    --card-white: #f7f7f5;
    --ink-navy: #1f2366;
    --ink-grey: #8a8a8e;
    --rule-grey: #b9b9bc;
    --back-deep: #25287a;
    --back-light: #6c69b4;
    --back-mark: rgba(255, 255, 255, 0.10);
  }
  * { box-sizing: border-box; margin: 0; padding: 0; }
  html, body {
    width: 1200px;
    height: 900px;
    overflow: hidden;
    background: var(--backdrop);
    font-family: "Jost", "Futura", sans-serif;
  }
  .canvas {
    width: 1200px;
    height: 900px;
    display: flex;
    flex-direction: column;
    align-items: center;
    justify-content: center;
    gap: 60px;
  }
  .card {
    width: 640px;
    height: 366px;
    position: relative;
    overflow: hidden;
    box-shadow: 0 10px 30px rgba(0, 0, 0, 0.45);
  }

  /* Back side */
  .card--back {
    background: linear-gradient(115deg, var(--back-deep) 0%, #3a3b92 45%, var(--back-light) 100%);
  }
  .back-wordmark {
    position: absolute;
    left: 24px;
    bottom: 18px;
    font-size: 190px;
    font-weight: 400;
    line-height: 1;
    letter-spacing: -2px;
    color: var(--back-mark);
    white-space: nowrap;
  }

  /* Front side */
  .card--front { background: var(--card-white); }
  .wordmark {
    position: absolute;
    left: 44px;
    top: 112px;
    font-size: 30px;
    font-weight: 400;
    color: var(--ink-navy);
    letter-spacing: 0.5px;
  }
  .holder {
    position: absolute;
    right: 40px;
    top: 118px;
    text-align: right;
  }
  .holder-name {
    font-size: 15px;
    font-weight: 600;
    color: var(--ink-navy);
    letter-spacing: 0.6px;
  }
  .holder-role {
    font-size: 13px;
    color: var(--ink-grey);
    letter-spacing: 0.4px;
  }
  .holder-rule {
    position: absolute;
    right: 40px;
    top: 160px;
    width: 330px;
    height: 1px;
    background: var(--rule-grey);
  }
  .contact {
    position: absolute;
    left: 44px;
    bottom: 30px;
    width: 330px;
    padding-top: 10px;
    border-top: 1px solid var(--rule-grey);
    font-size: 13px;
    line-height: 1.5;
    color: var(--ink-grey);
    letter-spacing: 0.3px;
  }
  .contact-label {
    font-weight: 600;
    color: #6f6f74;
  }
</style>
</head>
<body>
  <main class="canvas">
    <section class="card card--back" aria-label="Card back">
      <span class="back-wordmark">veltaro</span>
    </section>

    <section class="card card--front" aria-label="Card front">
      <div class="wordmark">veltaro holdings</div>
      <div class="holder">
        <p class="holder-name">Luis R. Andrade</p>
        <p class="holder-role">Director</p>
      </div>
      <div class="holder-rule"></div>
      <address class="contact" style="font-style: normal;">
        <p>Calle del Olmo Tardío 42 28017 Madrid</p>
        <p><span class="contact-label">T</span> +34 (91) 807-3356 <span class="contact-label">M</span> +34 (655) 718-904</p>
        <p><span class="contact-label">E</span> landrade@veltaroholdings.example</p>
      </address>
    </section>
  </main>
</body>
</html>
```